Need A Modern Website Design For ADSL2+ Provider

AIM: To sell affordable combined ADSL2+ Unlimited & phone line rentals to residential customers.

TYPE: This project is for DESIGN only (no code)

Source Files: I need all source files, fonts, images to be provided in ZIP format.

Logo: Existing (attached)

-Corporate Colours-
Black & Red (Same as Logo)
Others colours are fine as long as it looks corporate and modern.

-Pages-
Need another page to display our pricing plan

(1)Homepage Design
(2)Page to display our plans (needs to be in tables)
Example: http://lnkbrev.example/QwTr8k

-Pricing Plan-
(1) $59.95 / Month (Metro / City Areas)
(2) $79.95 / Month (Outside City Areas / Rural Areas)
Detailed Pricing plans is in PDF attached
Updates

Target Market(s)

Both male & female, Young & Old

Industry/Entity Type

Residential

Requirements
Must have
• + Graphic banner on the home page that shows our ADSL2+ combo plan for ADSL2+ Unlimited & Phone Line Rental for only $59.95

+ A box to allow customers to login to their account (username & password + login button)

+ Clearly display contact number
+ Button to sign up
+ Button to check service availability something like https://checkin.pelwara.example/wizard/

+ Button for Live Chat
+ Navigation menu
+ Social media icons Facebook, Google +, Twitter
+ Minimal text on homepage
+ Corporate & Friendly
Nice to have
• + Effective use of icons with corporate colours
+ Effective use of stockphotos
(use of people in photos would be nice)

+ Effective use of graphics to navigate people through the site and inform customers of specials,etc.
Should not have
• + Cluttered
+ Don’t want long scrolling homepage
+ Don’t want too much text on homepage 500 words is the estimate max.

```html
<!DOCTYPE html>
<html lang="en">
<head>
<meta charset="utf-8">
<title>Veltaro – Pairo2+ Plans</title>
<link rel="stylesheet" href="https://fonts.googleapis.com/css2?family=Jost:ital,wght@0,400;0,500;0,600;1,600;1,700&family=Signika:wght@600;700&family=Cinzel:wght@500&display=swap">
<style>
  :root {
    --ink: #231f20;
    --red: #e63c2f;
    --cyan: #3dbfe0;
    --band-dark: #1c1c1c;
    --band-mid: #555555;
    --row-grey: #d2d2d2;
    --text-dark: #2e2e2e;
    --social-blue: #2f5ea8;
    --white: #ffffff;
  }
  * { box-sizing: border-box; margin: 0; padding: 0; }
  html, body { width: 1200px; height: 909px; overflow: hidden; background: var(--white); }
  body { position: relative; font-family: "Jost", sans-serif; color: var(--ink); }

  .brand { position: absolute; left: 12px; top: 17px; display: flex; align-items: center; gap: 14px; }
  .brand-dot { width: 99px; height: 99px; border-radius: 50%; background: var(--ink); }
  .brand-name { font-family: "Cinzel", serif; font-weight: 500; font-size: 76px; line-height: 1; color: var(--ink); }

  .top-nav a, .foot-nav a { position: absolute; text-decoration: none; white-space: nowrap; }
  .top-nav a { top: 56px; font-size: 20px; color: var(--ink); }
  .top-nav .active::after, .foot-nav .active::after {
    content: ""; position: absolute; height: 5px; background: var(--red);
  }
  .top-nav .active::after { left: -12px; right: -8px; top: 30px; }
  .search { position: absolute; border: 2px solid #b5b5b5; border-radius: 12px; font-size: 15px; color: #9a9a9a; padding-left: 14px; line-height: 18px; }
  .search.top { left: 981px; top: 60px; width: 169px; height: 22px; }

  .band { position: absolute; left: 12px; width: 1183px; background: linear-gradient(100deg, var(--band-dark) 0%, var(--band-mid) 40%, #3a3a3a 60%, var(--band-mid) 80%, var(--band-dark) 100%); }
  .login-band { top: 131px; height: 84px; }
  .login-label { position: absolute; left: 30px; top: 28px; color: var(--white); font-size: 18px; }
  .field { position: absolute; left: 89px; width: 168px; height: 22px; background: var(--white); border-radius: 11px; color: var(--red); font-size: 15px; text-align: center; line-height: 22px; }
  .field.user { top: 15px; }
  .field.pass { top: 47px; }
  .go-btn { position: absolute; left: 269px; top: 26px; width: 37px; height: 33px; background: var(--cyan); color: var(--white); font-family: "Signika", sans-serif; font-weight: 700; font-size: 20px; text-align: center; line-height: 33px; }
  .contact { position: absolute; left: 846px; top: 28px; color: var(--white); font-size: 19px; }

  .promo { position: absolute; left: 0; top: 225px; width: 376px; font-family: "Signika", sans-serif; color: var(--text-dark); }
  .promo-title { position: absolute; left: 0; width: 376px; top: 52px; text-align: center; color: var(--red); font-size: 60px; line-height: 1.1; font-weight: 700; }
  .promo-lede { position: absolute; left: 29px; top: 125px; font-size: 21px; line-height: 25px; font-weight: 700; }
  .advantage-title { position: absolute; left: 0; width: 350px; top: 207px; text-align: center; font-size: 25px; font-weight: 700; }
  .advantage-list { position: absolute; left: 32px; top: 265px; list-style: none; font-family: "Jost", sans-serif; font-style: italic; font-weight: 700; font-size: 17px; line-height: 21.2px; }
  .advantage-list li::before { content: "•"; font-style: normal; margin-right: 3px; }
  .signup { position: absolute; left: 23px; top: 455px; font-size: 31px; font-weight: 700; }
  .signup-btn { position: absolute; left: 205px; top: 458px; width: 141px; height: 36px; background: var(--cyan); color: var(--white); font-size: 25px; font-weight: 700; text-align: center; line-height: 36px; border-radius: 3px; }

  .plans { position: absolute; left: 376px; top: 226px; width: 818px; border-collapse: collapse; table-layout: fixed; font-size: 14px; line-height: 17px; }
  .plans td { border: 1.5px solid var(--ink); vertical-align: top; padding: 3px 7px 0; }
  .plans td:not(:first-child) { text-align: center; }
  .plans tr.grey td { background: var(--row-grey); }
  .plans .head { font-weight: 600; }
  .plans .left { text-align: left !important; }

  .foot-band { top: 782px; height: 120px; }
  .search.foot { left: 82px; top: 21px; width: 168px; height: 22px; border-color: #888; color: #888; }
  .foot-nav a { top: 21px; font-size: 20px; color: var(--white); }
  .foot-nav .active::after { left: -12px; right: -12px; top: 32px; }
  .copyright { position: absolute; left: 0; width: 1262px; top: 71px; text-align: center; color: var(--white); font-size: 14px; line-height: 17px; }
  .follow { position: absolute; left: 1032px; top: 14px; width: 153px; height: 90px; background: var(--white); border-radius: 8px; }
  .follow-label { position: absolute; left: 0; width: 153px; top: 4px; text-align: center; color: var(--cyan); font-size: 16px; }
  .social { position: absolute; top: 32px; width: 47px; height: 46px; border-radius: 6px; }
  .social.one { left: 19px; background: var(--cyan); }
  .social.two { left: 71px; background: var(--social-blue); }
</style>
</head>
<body>
  <header>
    <div class="brand"><span class="brand-dot"></span><span class="brand-name">VELTARO</span></div>
    <nav class="top-nav">
      <a class="active" href="#" style="left:555px">Home</a>
      <a href="#" style="left:664px">About</a>
      <a href="#" style="left:767px">Plans</a>
      <a href="#" style="left:867px">Support</a>
    </nav>
    <div class="search top">Search for....</div>
  </header>

  <section class="band login-band">
    <span class="login-label">Login</span>
    <div class="field user">User Name</div>
    <div class="field pass">Password</div>
    <div class="go-btn">Go</div>
    <span class="contact">Contact us 1300 55-18-90</span>
  </section>

  <aside class="promo">
    <h1 class="promo-title">Pairo2+</h1>
    <p class="promo-lede">Pairo2+ offers line rental with<br>Unlimited ADSL2+ Broadband.</p>
    <h2 class="advantage-title">The Veltaro Advantage</h2>
    <ul class="advantage-list">
      <li>Free installation</li>
      <li>Unlimited ADSL2+</li>
      <li>line rental included</li>
      <li>WIFI Modem included</li>
      <li>Minimum Monthly Charge</li>
      <li>Low monthly administartion fee</li>
      <li>Local, long distance, and mobile calling</li>
    </ul>
    <span class="signup">Sign up now</span>
    <a class="signup-btn">Click here</a>
  </aside>

  <table class="plans">
    <colgroup><col style="width:259px"><col style="width:286px"><col style="width:273px"></colgroup>
    <tr style="height:60px"><td><span class="head">Pairo2+</span> Plans<br>Effective 1 January 2013</td><td><span class="head">Metro</span><br>On Net</td><td><span class="head">Regional</span><br>Off Net<br>(If Metro on-net not available)</td></tr>
    <tr class="grey" style="height:43px"><td>Minimum Monthly Charge, including line rental and Unlimited ADSL2+</td><td>$59.95</td><td>$79.95</td></tr>
    <tr style="height:26px"><td>Local Calls</td><td>18cents/call</td><td>18cents/call</td></tr>
    <tr class="grey" style="height:60px"><td>National Long Distance Calls (per minute)<br>Plus Cap National long Distance calls</td><td class="left">29cents or $1.89 for first 20 minutes then per minute rate applies</td><td class="left">29cents or $1.89 for first 20 minutes then per minute rate applies</td></tr>
    <tr style="height:42px"><td>Calls to Mobiles within Australia Plus Cap Calls to mobile</td><td class="left">35cents or $3.40 for the first 20 minutes then per minute rate applies</td><td class="left">35cents or $3.40 for the first 20 minutes then per minute rate applies</td></tr>
    <tr class="grey" style="height:26px"><td>13/1300 Calls per call</td><td>44cents</td><td>44cents</td></tr>
    <tr style="height:29px"><td>International calls</td><td>Refer standard rates sheet</td><td>Refer standard rates sheet</td></tr>
    <tr class="grey" style="height:26px"><td>Call Connection fee (timed calls)</td><td>39 cents per call</td><td>39 cents per call</td></tr>
    <tr style="height:26px"><td>Contract term</td><td>24months</td><td>24months</td></tr>
    <tr class="grey" style="height:25px"><td>Minimum 24 month contract</td><td>$1,463.75</td><td>$1,943.75</td></tr>
    <tr style="height:26px"><td>WIFI Modem (included in cost)</td><td>No Charge</td><td>No Charge</td></tr>
    <tr class="grey" style="height:25px"><td>Delivery and Handling fee of Modem</td><td>One off charge of $24.95</td><td>One off charge of $24.95</td></tr>
    <tr style="height:26px"><td>Set up fee</td><td>No Charge</td><td>No Charge</td></tr>
    <tr class="grey" style="height:59px"><td>Termination fee</td><td>$250 if any part of service is cancelled or transferred before the end of the 24 month term</td><td>$250 if any part of service is cancelled or transferred before the end of the 24 month term</td></tr>
    <tr style="height:43px"><td>Administration fee (per month)</td><td>$10 administration fee if pre-selected to other service provider</td><td>$10 administration fee if pre-selected to other service provider</td></tr>
  </table>

  <footer class="band foot-band">
    <div class="search foot">Search for....</div>
    <nav class="foot-nav">
      <a class="active" href="#" style="left:299px">Home</a>
      <a href="#" style="left:409px">About</a>
      <a href="#" style="left:513px">Plans</a>
      <a href="#" style="left:612px">Support</a>
      <a href="#" style="left:726px">Contact us</a>
      <a href="#" style="left:859px">Mobile Site</a>
    </nav>
    <p class="copyright">Veltaro Communication and Information Services Pty Limited ABN<br>2013 all rights reserved</p>
    <div class="follow">
      <span class="follow-label">Follow us</span>
      <span class="social one" role="img" aria-label="Social network link"></span>
      <span class="social two" role="img" aria-label="Social network link"></span>
    </div>
  </footer>
</body>
</html>
```